Qkb

Spa brochure (tri-fold or bi-fold layout)

Target Market(s)

18-99 yrs old

Font styles to use
Sans Serif
Decorative

Colors
00a990
33b8a4
86cfc6
ffffff

Requirements
Must have
• high end appeal, larger font for ease of reading info, flow smoothly through all departments (massage, facials/waxing, nails, vichy and hair)
Nice to have
• map with address
Should not have
• confusion or spelling errors

```html
<!DOCTYPE html>
<html lang="en">
<head>
<meta charset="utf-8">
<title>Qkb Day Spa Brochure</title>
<link rel="stylesheet" href="https://fonts.googleapis.com/css2?family=Open+Sans:wght@400;600&family=Roboto:wght@300;400&display=swap">
<style>
  :root {
    --teal: #17958c;
    --teal-light: #33b8a4;
    --teal-pale: #86cfc6;
    --paper: #f1f1f1;
    --ink: #2a2a2a;
    --panel-dark: rgba(32, 32, 34, 0.88);
    --stage: #d4d3d4;
    --white: #ffffff;
  }
  * { box-sizing: border-box; margin: 0; padding: 0; }
  html, body { width: 1200px; height: 1200px; overflow: hidden; }
  body { background: var(--stage); font-family: "Open Sans", sans-serif; color: var(--ink); position: relative; }

  .brochure { position: absolute; left: 30px; top: 165px; width: 1140px; height: 870px; display: flex; background: var(--paper); }
  .panel { position: relative; width: 380px; height: 870px; overflow: hidden; }

  /* Left panel */
  .series { background: var(--paper); }
  .team-photo { position: absolute; left: 14px; top: 0; width: 366px; height: 316px;
    background: linear-gradient(180deg, #6d6a68 0%, #a9a4a0 45%, #57534f 100%); }
  .band { background: var(--teal); color: var(--white); font-family: "Roboto", sans-serif; font-weight: 300; }
  .series-band { position: absolute; left: 14px; top: 316px; width: 366px; height: 52px;
    display: flex; align-items: center; justify-content: center; font-size: 23px; }
  .series-body { position: absolute; left: 46px; right: 30px; top: 382px; }
  .series-intro { font-size: 14.4px; line-height: 17px; text-align: justify; }
  .series-list { list-style: none; margin: 18px 0 0 14px; }
  .series-list li { position: relative; font-size: 13.6px; line-height: 17px; margin-bottom: 9px; padding-left: 10px; }
  .series-list li::before { content: ""; position: absolute; left: 0; top: 6px; width: 5px; height: 5px; border-radius: 50%; background: var(--teal); }
  .policy-title { color: var(--teal); font-size: 15px; text-align: center; margin-top: 22px; }
  .policy-text { font-size: 11.4px; line-height: 13.6px; text-align: justify; margin-top: 4px; }

  /* Middle panel */
  .contact { background: #3c4248; }
  .contact-photo { position: absolute; inset: 0;
    background: linear-gradient(180deg, #3a2a2e 0%, #8c4a5c 18%, #c98a9c 32%, #d9d4d2 48%, #8a97a4 58%, #6b7884 72%, #c2b8a8 80%, #2f5a2c 88%, #4a6a38 100%); }
  .contact-column { position: absolute; left: 74px; top: 0; width: 228px; height: 760px; background: var(--panel-dark); color: var(--white); text-align: center; }
  .about-title { font-family: "Roboto", sans-serif; font-weight: 300; font-size: 17px; margin-top: 26px; }
  .about-text { font-size: 7.4px; line-height: 9px; text-align: justify; margin: 8px 26px 0; }
  .logo-box { position: absolute; left: 54px; top: 226px; width: 270px; height: 110px;
    display: flex; align-items: center; justify-content: center; gap: 12px; font-size: 40px; }
  .logo-dot { width: 16px; height: 16px; border-radius: 50%; background: var(--white); }
  .contact-info { position: absolute; left: 0; right: 0; top: 355px; font-family: "Roboto", sans-serif; font-weight: 300; }
  .contact-lead { font-size: 13.5px; line-height: 16px; }
  .label { font-size: 10.5px; margin-top: 14px; }
  .phone { font-size: 19px; margin-top: 2px; }
  .address { font-size: 11px; margin-top: 4px; }
  .hours { font-size: 11.4px; line-height: 13.6px; margin-top: 10px; }
  .web { font-size: 16px; margin-top: 14px; }
  .social-pill { display: inline-flex; gap: 4px; background: var(--teal); border-radius: 12px; padding: 5px 16px; margin-top: 8px; }
  .social-pill span { width: 11px; height: 11px; border-radius: 50%; background: var(--white); }
  .gift-card { position: absolute; left: 20px; top: 612px; width: 188px; height: 76px; background: var(--white); border: 2px solid var(--teal-pale); }
  .gift-art { position: absolute; left: 4px; top: 4px; width: 50px; height: 66px; background: linear-gradient(135deg, var(--teal-pale), var(--teal-light)); opacity: .7; }
  .gift-name { position: absolute; left: 24px; top: 5px; color: var(--teal-light); font-size: 8.5px; }
  .gift-heading { position: absolute; right: 8px; top: 4px; color: var(--teal-light); font-size: 9.5px; }
  .gift-line { position: absolute; left: 58px; right: 6px; height: 1px; background: var(--teal-pale); }
  .gift-copy { position: absolute; left: 26px; right: 26px; top: 700px; font-size: 7.6px; line-height: 9px; text-align: justify; }

  /* Right panel */
  .cover { background: var(--paper); }
  .brand { position: absolute; left: 0; right: 0; top: 58px; display: flex; align-items: center; justify-content: center; gap: 14px;
    color: var(--teal); font-family: "Roboto", sans-serif; font-weight: 300; font-size: 58px; }
  .brand-dot { width: 22px; height: 22px; border-radius: 50%; background: var(--teal); }
  .cover-band { position: absolute; left: 0; top: 184px; width: 380px; height: 90px; display: flex; align-items: center; justify-content: center; text-align: center;
    font-size: 24px; line-height: 26px; }
  .tagline { position: absolute; left: 0; right: 0; top: 296px; text-align: center; color: var(--teal); font-family: "Roboto", sans-serif; font-weight: 300; font-size: 17px; line-height: 20px; }
  .stones-photo { position: absolute; left: 0; top: 350px; width: 380px; height: 520px;
    background: linear-gradient(180deg, #eeeeee 0%, #a5785a 18%, #8a6448 28%, #e6e3df 42%, #c9c3bc 60%, #3b3631 78%, #2a2622 100%); }
  .web-pill { position: absolute; left: 4px; bottom: 24px; background: rgba(20,20,20,.85); color: var(--white); font-family: "Roboto", sans-serif; font-size: 12px; padding: 3px 6px; border-radius: 3px; }
  .icon-pill { position: absolute; right: 8px; bottom: 26px; display: flex; gap: 3px; background: rgba(20,20,20,.85); padding: 4px 6px; border-radius: 8px; }
  .icon-pill span { width: 8px; height: 8px; border-radius: 50%; background: var(--white); }
</style>
</head>
<body>
<div class="brochure">

  <section class="panel series">
    <div class="team-photo" role="img" aria-label="Black and white photo of the spa team standing together in the salon"></div>
    <h2 class="band series-band">OUR SERIES</h2>
    <div class="series-body">
      <p class="series-intro">Our Qkb Team is committed to making your visit enjoyable and affordable. For this reason, we offer a series for many of the high-demand services we offer. A series features the same attentive care provided in all of our sessions as well as a price reduction when services are purchased in advance to show our appreciation for the continued loyalty of our valued customers.</p>
      <ul class="series-list">
        <li>6 Goddess Facials (60 min) for $450/6 Goddess Facials (90 min) for $625</li>
        <li>6 Signature Massages (60 min) for $450/6 Signature Massages (90 min) for $625</li>
        <li>6 Sports Massages (60 min) for $500/6 Sports Massages (90 min) for $700</li>
        <li>5 Infra-Red Sauna Sessions for $90/10 Infra-Red Sauna Sessions for $170</li>
      </ul>
      <h3 class="policy-title">Cancellation and No-show Policy</h3>
      <p class="policy-text">Please allow at least 24-hours notice for cancellations or changes. We require a credit card in order to book an appointment. Cancellations less than 24-hours in advance will result in a charge equaling 50% of the service cost. No-shows will be charged the full value of the service.</p>
    </div>
  </section>

  <section class="panel contact">
    <div class="contact-photo" role="img" aria-label="Photo of nail polish bottles above a lakeside view with boats, beach and garden"></div>
    <div class="contact-column">
      <h2 class="about-title">ABOUT IS</h2>
      <p class="about-text">The Qkb Day Spa is a holistic and organic boutique style spa. Our spa provides an elegant, relaxing, and healing atmosphere for our clients. There is a spiritual aspect to the services we provide, based on the quote, "In beauty may we walk." At Qkb, your experience will be memorable, leaving you refreshed, beautiful, balanced, and nourished. Our staff is comprised of highly trained therapists, estheticians, hair stylists, and aromatherapy practitioners, the best in Lakeside, earning the "Best Day Spa" category in Cedar County 4 years and running. We offer a full range of holistic services including massages, facials, hair appointments, and esthetician treatments.</p>
      <div class="contact-info">
        <p class="contact-lead">To make an appointment or<br>if you have any questions,</p>
        <p class="label">PLEASE CALL US AT:</p>
        <p class="phone">555-014-2290</p>
        <p class="label">ADDRESS</p>
        <p class="address">88 Lakeview Ave</p>
        <p class="hours">We are open 7 days a week from<br>9-5 by appointment and outside<br>of our normal hours by request.</p>
        <p class="web">qkbdayspa.example</p>
        <div class="social-pill"><span></span><span></span><span></span></div>
      </div>
      <div class="gift-card">
        <div class="gift-art" role="img" aria-label="Teal floral illustration"></div>
        <span class="gift-name">QKB Day Spa</span>
        <span class="gift-heading">Gift Certificate</span>
        <div class="gift-line" style="top:30px"></div>
        <div class="gift-line" style="top:40px"></div>
        <div class="gift-line" style="top:50px"></div>
        <div class="gift-line" style="top:60px"></div>
      </div>
      <p class="gift-copy">Looking for a great gift for everyone on your list? Spa gift certificates for Qkb services or products are sure to make everyone feel special. They are available online in several denominations.</p>
    </div>
    <div class="band logo-box"><span class="logo-dot"></span>Qkb</div>
  </section>

  <section class="panel cover">
    <div class="brand"><span class="brand-dot"></span>Qkb</div>
    <h1 class="band cover-band">BEAUTY WITH ELEGANT<br>RELAXING AND HEALING</h1>
    <p class="tagline">• RECONNECT • REJUVENATE<br>• RELAX • REFRESH</p>
    <div class="stones-photo" role="img" aria-label="Photo of a stack of smooth dark stones by the water"></div>
    <span class="web-pill">qkbdayspa.example</span>
    <div class="icon-pill"><span></span><span></span><span></span></div>
  </section>

</div>
</body>
</html>
```